Flyer Design Project

I need a flyer designed in postcard size for a meditation class.

I want it to look arty and different.

The front should have a picture that depicts chocolate and meditation with the chocolate part being more eye catching. It should just read Amber Quietude.

The back should have the details of the cousre. See the attached wrod doc.

anyone who loves chocolate

• a dark choclate theme but not too dark that it looks dreary. It should look peaceful and modern but elegant.

My logo should be displayed on the leaflet somewhere.
• Clear and uncluttered
• Cheesy cliched images. I want something original.

```html
<!DOCTYPE html>
<html lang="en">
<head>
<meta charset="utf-8">
<title>Amber Quietude – Flyer</title>
<link rel="stylesheet" href="https://fonts.googleapis.com/css2?family=Questrial&family=Didact+Gothic&family=Varela+Round&display=swap">
<style>
  :root {
    --olive: #b3a955;
    --cocoa: #6e3f33;
    --cocoa-dark: #3e1f16;
    --cocoa-deep: #4a2619;
    --paper: #ffffff;
    --frame: #3a3a3a;
  }
  * { margin: 0; padding: 0; box-sizing: border-box; }
  html, body { width: 1200px; height: 832px; overflow: hidden; background: var(--paper); }
  .canvas { position: relative; width: 1200px; height: 832px; }

  .card {
    position: absolute; top: 19px; height: 789px;
    border: 1px solid var(--frame); background: var(--paper); overflow: hidden;
  }
  .card--front { left: 47px; width: 542px; }
  .card--back { left: 609px; width: 578px; }

  .display-title {
    font-family: "Questrial", sans-serif; color: var(--olive);
    font-weight: 400; line-height: 0.84;
    -webkit-text-stroke: 1.4px var(--olive);
  }
  .display-title span { display: block; }

  /* front */
  .front-bar { position: absolute; left: 0; top: 37px; width: 44px; height: 115px; background: var(--olive); }
  .front-title { position: absolute; left: 56px; top: 40px; font-size: 66px; letter-spacing: 0.5px; }
  .front-photo {
    position: absolute; left: 0; top: 206px; width: 440px; height: 550px;
    background:
      radial-gradient(ellipse 55% 42% at 42% 40%, var(--cocoa-deep) 0%, var(--cocoa) 40%, rgba(110,63,51,0.5) 70%, rgba(255,255,255,0) 100%),
      radial-gradient(ellipse 40% 32% at 55% 72%, rgba(74,38,25,0.8) 0%, rgba(110,63,51,0.4) 55%, rgba(255,255,255,0) 100%);
  }
  .front-brand {
    position: absolute; left: 440px; top: 612px; width: 80px;
    display: flex; flex-direction: column; align-items: center; gap: 8px;
    font-family: "Didact Gothic", sans-serif; color: var(--olive);
    font-size: 14px; line-height: 1.15; text-align: center;
  }
  .front-brand .mark { width: 56px; height: 56px; background: var(--olive); }

  /* back */
  .back-title { position: absolute; left: 38px; top: 36px; font-size: 64px; width: 384px; letter-spacing: 0.5px; }
  .back-title .course { text-align: right; }

  .section { position: absolute; left: 0; font-family: "Didact Gothic", sans-serif; color: var(--cocoa); }
  .section-label {
    display: inline-block; background: var(--olive); color: var(--cocoa-dark);
    font-family: "Didact Gothic", sans-serif; font-weight: 400; font-size: 15.5px;
    padding: 0 8px 0 31px; line-height: 18px; letter-spacing: 0.4px;
  }
  .section-body { width: 505px; padding-left: 31px; font-size: 16.3px; line-height: 21px; letter-spacing: 0.55px; }
  .section--intro { top: 212px; }
  .section--weight { top: 359px; }
  .section--includes { top: 505px; }
  .perks { list-style: none; }
  .perks li::before { content: "• "; }

  .contact {
    position: absolute; left: 232px; top: 704px;
    font-family: "Didact Gothic", sans-serif; font-style: normal; color: var(--cocoa);
    font-size: 14.5px; line-height: 21px; letter-spacing: 0.3px;
  }
</style>
</head>
<body>
<main class="canvas">
  <section class="card card--front">
    <div class="front-bar"></div>
    <h1 class="display-title front-title"><span>amber</span><span>QUIETUDE</span></h1>
    <div class="front-photo" role="img" aria-label="Photograph of dark chocolate curls and shavings"></div>
    <div class="front-brand"><span class="mark"></span><span>Lumen Grove Studio</span></div>
  </section>

  <section class="card card--back">
    <h2 class="display-title back-title"><span>amber</span><span>QUIETUDE</span><span class="course">course</span></h2>

    <div class="section section--intro">
      <h3 class="section-label">Amber What?!</h3>
      <p class="section-body">Yes you read right. Amber Quietude! What could be better than combining the dilatable taste of chocolate with meditation, right? Well that is exactly what this course is all about with a little bit of Mindfulness thrown in.</p>
    </div>

    <div class="section section--weight">
      <h3 class="section-label">Learn to Eat Chocolate without gaining weight!</h3>
      <p class="section-body">What do you mean? I already know how to eat Choco-late.” We challenge you that you have in fact not really eaten chocolate. So we are going to teach you how to do it mindfully. This way you are guaranteed not to gain weight while eating chocolate.</p>
    </div>

    <div class="section section--includes">
      <h3 class="section-label">What you get with the course:</h3>
      <div class="section-body">
        <ul class="perks">
          <li>An Amber Quietude course book.</li>
          <li>Mindfulness and meditation instruction online.</li>
          <li>Learn how to eat chocolate mindfully.</li>
          <li>Learn Meditation techniques and postures.</li>
          <li>FREE mp3 Guided Meditation download.</li>
          <li>5% of the course goes to charity –</li>
        </ul>
        <p>Please see our website for this month’s charitable cause.</p>
      </div>
    </div>

    <address class="contact">
      www.amberquietude.com.au<br>
      Brought to you by Lumen Grove Studio<br>
      Phone (02) 5550 1847
    </address>
  </section>
</main>
</body>
</html>
```